Business Card Design

Professional solutions in (servers, security, networks, programming)

Industry/Entity Type

Business

Contact Information for Business Card

Nadim Fouzan
Internet services and network solutions
TDK - GLPW - GLPT
netdesk@kavo-lin.com / 05291473806
www.kavo-lin.com

```html
<!DOCTYPE html>
<html lang="en">
<head>
<meta charset="utf-8">
<title>Nadim Fouzan – Business Card</title>
<link rel="stylesheet" href="https://fonts.googleapis.com/css2?family=Arimo:wght@700&family=Share+Tech+Mono&display=swap">
<style>
  :root {
    --card-blue: #134bff;
    --ink-white: #ffffff;
  }
  html, body {
    margin: 0;
    padding: 0;
    width: 1200px;
    height: 702px;
    overflow: hidden;
    background: var(--card-blue);
  }
  .card {
    display: block;
    width: 1200px;
    height: 702px;
  }
  .card-bg { fill: var(--card-blue); }
  .holder-name {
    font-family: "Arimo", "Helvetica Neue", Arial, sans-serif;
    font-weight: 700;
    font-size: 150px;
    letter-spacing: -1px;
    fill: var(--ink-white);
  }
  .tagline {
    font-family: "Share Tech Mono", monospace;
    font-size: 41px;
    fill: var(--ink-white);
  }
  .tagline-rule {
    stroke: var(--ink-white);
    stroke-width: 1.5;
  }
  .certifications {
    font-family: "Share Tech Mono", monospace;
    font-size: 44px;
    letter-spacing: 8px;
    fill: var(--ink-white);
  }
  .contact-line {
    font-family: "Arimo", "Helvetica Neue", Arial, sans-serif;
    font-weight: 700;
    font-size: 39px;
    fill: var(--ink-white);
  }
</style>
</head>
<body>
<svg class="card" viewBox="0 0 1200 702" xmlns="http://www.w3.org/2000/svg">
  <rect class="card-bg" x="0" y="0" width="1200" height="702"/>

  <text class="holder-name" x="60" y="171">Nadim Fouzan</text>

  <text class="tagline" x="83" y="333">Internet services and network solutions</text>
  <line class="tagline-rule" x1="0" y1="339" x2="1045" y2="339"/>
  <text class="certifications" x="83" y="375">TDK-GLPW-GLPT</text>

  <text class="contact-line" x="63" y="536">netdesk@kavo-lin.com</text>
  <text class="contact-line" x="63" y="586">05291473806</text>
  <text class="contact-line" x="63" y="630">www.kavo-lin.com</text>
</svg>
</body>
</html>
```